Marrowfield Systems Business Card

I am a managed service provider and general business technology partner for all IT services. I really enjoy design layout of https://www.pixelbazaar-demo.com/design/40627718 and would like something like this but focus graphically a little more on the constellation kind of images. I have provided my logo I want to use I own the rights to it. On the front I would like the tag line to be "Simple Solutions for Complex Connections" With the logo and attached background. The information side in the bottom left I would like "We Make IT Happen." the Logo how they did it twice I think looks great. Marrowfield Systems LLC for the Business name. My Name is Garrett Holloway M.S. Owner
Email: Garrett@Marrowfield-Sys.example
Cell: 555-214-3796

I look forward to seeing your work

Font styles to use
Serif

```html
<!DOCTYPE html>
<html lang="en">
<head>
<meta charset="utf-8">
<title>Marrowfield Systems Business Card</title>
<link href="https://fonts.googleapis.com/css2?family=Libre+Baskerville:wght@400;700&display=swap" rel="stylesheet">
<style>
  :root {
    --canvas: #2a2a2c;
    --card: #141414;
    --white: #ffffff;
    --grey: #b9b9b9;
    --orange: #f26522;
    --amber: #fbb415;
    --blue: #0a9be0;
    --blue-deep: #0667b8;
  }
  * { margin: 0; padding: 0; box-sizing: border-box; }
  html, body { width: 1200px; height: 1015px; overflow: hidden; }
  body {
    background: var(--canvas);
    font-family: "Libre Baskerville", serif;
    position: relative;
  }
  .card {
    position: absolute;
    left: 250px;
    width: 700px;
    height: 400px;
    background: var(--card);
    overflow: hidden;
    box-shadow: 0 12px 30px rgba(0,0,0,.55);
  }
  .card--front { top: 75px; }
  .card--back { top: 540px; }

  /* front */
  .constellation-field {
    position: absolute;
    right: 0;
    top: 0;
    width: 460px;
    height: 270px;
    background:
      radial-gradient(ellipse at 30% 40%, rgba(10,155,224,.35) 0%, rgba(10,155,224,0) 55%),
      radial-gradient(ellipse at 70% 55%, rgba(242,101,34,.30) 0%, rgba(251,180,21,.12) 35%, rgba(251,180,21,0) 65%);
  }
  .front-mark {
    position: absolute;
    right: 60px;
    top: 100px;
    display: flex;
    align-items: center;
    gap: 16px;
  }
  .front-mark__dot {
    width: 56px; height: 56px; border-radius: 50%;
    background: var(--orange);
    flex: none;
  }
  .front-mark__name {
    color: var(--white);
    font-weight: 700;
    font-size: 26px;
    letter-spacing: 1px;
    text-transform: uppercase;
  }
  .front-identity {
    position: absolute;
    left: 50px;
    bottom: 50px;
  }
  .company {
    color: var(--white);
    font-weight: 700;
    font-size: 23px;
    letter-spacing: 1px;
    text-transform: uppercase;
    white-space: nowrap;
  }
  .tagline {
    color: var(--grey);
    font-weight: 400;
    font-size: 11.5px;
    letter-spacing: 2px;
    text-transform: uppercase;
    margin-top: 6px;
    white-space: nowrap;
  }

  /* back */
  .network-texture {
    position: absolute;
    right: 0; top: 0;
    width: 440px; height: 230px;
    background: radial-gradient(ellipse at 70% 30%, #272727 0%, #1c1c1c 45%, var(--card) 80%);
  }
  .back-identity {
    position: absolute;
    left: 90px;
    top: 95px;
    display: flex;
    align-items: center;
    gap: 18px;
  }
  .back-identity__dot {
    width: 56px; height: 56px; border-radius: 50%;
    background: var(--blue);
    flex: none;
  }
  .back-identity .company { font-size: 19px; }
  .back-identity .tagline { font-size: 9.5px; letter-spacing: 1.6px; margin-top: 4px; }

  .person {
    position: absolute;
    left: 90px;
    top: 185px;
  }
  .person__name {
    font-weight: 700;
    font-size: 24px;
    letter-spacing: .5px;
    text-transform: uppercase;
    white-space: nowrap;
    background: linear-gradient(90deg, var(--amber), var(--orange));
    -webkit-background-clip: text;
    background-clip: text;
    color: transparent;
  }
  .person__role {
    color: var(--grey);
    font-size: 16px;
    letter-spacing: 1px;
    text-transform: uppercase;
    margin-top: 4px;
  }
  .contact {
    list-style: none;
    margin-top: 10px;
  }
  .contact li {
    display: flex;
    align-items: center;
    gap: 10px;
    color: var(--grey);
    font-size: 14px;
    line-height: 22px;
    white-space: nowrap;
  }
  .contact svg { width: 16px; height: 16px; flex: none; }

  .slogan-band {
    position: absolute;
    left: 0; bottom: 0;
    width: 390px; height: 48px;
    background: linear-gradient(90deg, var(--blue), var(--blue-deep));
    clip-path: polygon(0 0, 340px 0, 390px 100%, 0 100%);
    display: flex;
    align-items: center;
    padding-left: 90px;
    color: var(--white);
    font-weight: 700;
    font-size: 15px;
    letter-spacing: 1px;
    text-transform: uppercase;
    white-space: nowrap;
  }
  .web-band {
    position: absolute;
    right: 0; bottom: 0;
    width: 320px; height: 18px;
    background: linear-gradient(90deg, var(--amber), #fcc21b);
    clip-path: polygon(0 0, 100% 0, 100% 100%, 22px 100%);
  }
  .website {
    position: absolute;
    right: 40px;
    bottom: 28px;
    color: var(--orange);
    font-size: 14px;
    white-space: nowrap;
  }
</style>
</head>
<body>

<section class="card card--front">
  <div class="constellation-field" role="img" aria-label="Constellation network background in blue and orange tones"></div>
  <div class="front-mark">
    <span class="front-mark__dot"></span>
    <span class="front-mark__name">Marrowfield Systems</span>
  </div>
  <div class="front-identity">
    <p class="company">Marrowfield Systems LLC</p>
    <p class="tagline">Simple Solutions for Complex Connections</p>
  </div>
</section>

<section class="card card--back">
  <div class="network-texture" role="img" aria-label="Faint constellation network texture"></div>

  <div class="back-identity">
    <span class="back-identity__dot"></span>
    <div>
      <p class="company">Marrowfield Systems LLC</p>
      <p class="tagline">Simple Solutions for Complex Connections</p>
    </div>
  </div>

  <div class="person">
    <p class="person__name">Garrett Holloway M.S.</p>
    <p class="person__role">Owner</p>
    <ul class="contact">
      <li>
        <svg viewBox="0 0 16 16"><path d="M4 1.5 6.2 4 5 5.6c.9 2 2.4 3.5 4.4 4.4L11 8.8l2.5 2.2-1.4 2.5C7 13.3 2.7 9 2.5 3z" fill="none" stroke="#f26522" stroke-width="1.6" stroke-linejoin="round"/></svg>
        555-214-3796
      </li>
      <li>
        <svg viewBox="0 0 16 16"><rect x="4" y="1.5" width="8" height="13" rx="1.5" fill="none" stroke="#f26522" stroke-width="1.6"/><line x1="7" y1="12" x2="9" y2="12" stroke="#f26522" stroke-width="1.4"/></svg>
        555-214-3796
      </li>
      <li>
        <svg viewBox="0 0 16 16"><rect x="1.5" y="3.5" width="13" height="9" fill="#f26522"/><path d="M1.5 3.5 8 9l6.5-5.5" fill="none" stroke="#141414" stroke-width="1.3"/></svg>
        Garrett@Marrowfield-Sys.example
      </li>
    </ul>
  </div>

  <div class="slogan-band">We Make IT Happen</div>
  <p class="website">www.Marrowfield-Sys.example</p>
  <div class="web-band"></div>
</section>

</body>
</html>
```